Staffing Company Website

We need a website for a new company based out of central California called "Harbor Field Staffing". We staff truck drivers for agriculture trucking businesses. We don't want a super corporate feel, we want something that feels more inviting to the kind of person who would work in Agriculture/Trucking while still being professional. Please let me know if you have any questions

```html
<!DOCTYPE html>
<html lang="en">
<head>
<meta charset="utf-8">
<title>Harbor Field Staffing</title>
<link href="https://fonts.googleapis.com/css2?family=Montserrat:wght@500;600;700;800&family=Lato:ital,wght@0,400;0,700;1,400&family=Jost:wght@400;500&display=swap" rel="stylesheet">
<style>
  :root {
    --ink: #000000;
    --text: #3a3a3a;
    --muted: #555555;
    --white: #ffffff;
    --paper: #f1f1f1;
    --field: #b98a3c;
    --sky: #8fb2cc;
  }
  * { box-sizing: border-box; margin: 0; padding: 0; }
  html, body { width: 1200px; height: 3250px; overflow: hidden; }
  body {
    font-family: "Lato", sans-serif; color: var(--text); background: var(--white); position: relative;
    -webkit-font-smoothing: antialiased; -moz-osx-font-smoothing: grayscale; text-rendering: geometricPrecision;
  }
  .abs { position: absolute; }
  .heading { font-family: "Montserrat", sans-serif; font-weight: 800; color: var(--ink); letter-spacing: 0.5px; }
  .btn {
    position: absolute; display: flex; align-items: center; justify-content: center;
    background: var(--ink); color: var(--white); font-family: "Montserrat", sans-serif;
    font-weight: 700; font-size: 14px; text-decoration: none;
    border-radius: 6px 24px 24px 24px;
  }
  .copy { font-size: 15.5px; line-height: 28px; color: var(--muted); }
  .copy p, .post p, .service p { color: inherit; }

  /* Header */
  .site-header { position: absolute; left: 0; top: 0; width: 1200px; height: 98px; background: var(--ink); }
  .brand { position: absolute; display: flex; align-items: center; gap: 14px; color: var(--white); font-family: "Montserrat", sans-serif; font-weight: 600; }
  .brand-mark { border: 3px solid var(--white); }
  .site-header .brand { left: 111px; top: 14px; font-size: 17px; line-height: 21px; }
  .site-header .brand-mark { width: 56px; height: 56px; }
  .nav { position: absolute; left: 521px; top: 40px; display: flex; gap: 27px; font-family: "Jost", sans-serif; font-size: 15px; color: var(--white); }
  .nav a { color: var(--white); text-decoration: none; }
  .nav a.active { font-weight: 500; }
  .header-cta { left: 953px; top: 28px; width: 136px; height: 43px; border: 2px solid var(--white); background: var(--ink); border-radius: 4px 18px 4px 18px; }

  /* Hero */
  .hero { position: absolute; left: 0; top: 98px; width: 1200px; height: 412px; }
  .hero-photo { position: absolute; inset: 0; background: linear-gradient(180deg, var(--sky) 0%, #c8c3b0 38%, #c89a48 52%, var(--field) 75%, #8a6227 100%); }
  .hero-shade { position: absolute; inset: 0; background: linear-gradient(90deg, rgba(40,28,10,0.75) 0%, rgba(40,28,10,0.35) 45%, rgba(0,0,0,0) 70%); }
  .hero-kicker { left: 111px; top: 52px; font-family: "Montserrat", sans-serif; font-weight: 600; font-size: 24px; color: var(--white); }
  .hero-title { left: 111px; top: 88px; font-size: 57px; line-height: 62px; color: var(--white); }
  .hero-text { left: 111px; top: 219px; font-family: "Jost", sans-serif; font-size: 17.5px; line-height: 28px; color: var(--white); }
  .hero .btn { left: 111px; top: 291px; width: 138px; height: 44px; }

  /* About */
  .about-photo { left: 112px; top: 582px; width: 413px; height: 449px; border-bottom-right-radius: 230px; background: linear-gradient(135deg, #d9d9d6 0%, #a9a58c 45%, #4d5a47 75%, #2a2e2a 100%); overflow: hidden; }
  .frame { position: absolute; border: 2px solid var(--white); }
  .about-photo .frame { left: 16px; top: 16px; right: 16px; bottom: 16px; border-bottom-right-radius: 210px; }
  .about-title { left: 622px; top: 598px; font-size: 45px; }
  .about-lead { left: 622px; top: 664px; width: 470px; font-style: italic; font-size: 18.5px; line-height: 28px; color: var(--ink); }
  .about-copy { left: 622px; top: 730px; width: 470px; }
  .about-copy p + p { margin-top: 13px; }
  .about-btn { left: 622px; top: 939px; width: 138px; height: 43px; }

  /* Services */
  .services { position: absolute; left: 0; top: 1087px; width: 1200px; height: 651px; background: var(--paper); border-bottom-left-radius: 260px; }
  .services-title { left: 0; width: 1200px; top: 60px; text-align: center; font-size: 45px; }
  .service { position: absolute; top: 166px; width: 304px; text-align: center; }
  .service-photo { width: 304px; height: 246px; }
  .service h3 { margin-top: 34px; font-family: "Montserrat", sans-serif; font-weight: 600; font-size: 17.5px; line-height: 24px; color: #2b2b2b; }
  .service p { margin-top: 4px; font-size: 15px; line-height: 28px; color: var(--muted); }
  .arrow { position: absolute; top: 437px; }

  /* Why */
  .why-title { left: 112px; top: 1902px; font-size: 45px; }
  .why-copy { left: 112px; top: 1977px; width: 480px; }
  .why-copy p + p { margin-top: 13px; }
  .why-btn { left: 112px; top: 2186px; width: 138px; height: 44px; }
  .why-photo { left: 676px; top: 1829px; width: 413px; height: 449px; border-top-left-radius: 230px; background: linear-gradient(160deg, #3e3b36 0%, #7c8796 40%, #a2b3c7 65%, #3a4a7a 100%); overflow: hidden; }
  .why-photo .frame { left: 16px; top: 16px; right: 16px; bottom: 16px; border-top-left-radius: 210px; }

  /* Blog + footer */
  .lower { position: absolute; left: 0; top: 2361px; width: 1200px; height: 889px; background: var(--ink); }
  .blog { position: absolute; left: 0; top: 0; width: 1200px; height: 569px; background: var(--paper); border-bottom-right-radius: 260px 300px; }
  .blog-title { left: 0; width: 1200px; top: 80px; text-align: center; font-size: 45px; }
  .post { position: absolute; top: 169px; width: 308px; height: 312px; background: var(--white); border-left: 1px solid var(--ink); padding: 34px 28px 0 28px; }
  .post::before { content: ""; position: absolute; left: -3px; top: 44px; width: 4px; height: 38px; background: var(--ink); }
  .post h3 { font-family: "Lato", sans-serif; font-weight: 400; font-size: 19.5px; line-height: 29px; color: #333; }
  .post time { display: block; margin-top: 16px; font-size: 14px; color: #666; }
  .post p { margin-top: 18px; font-size: 15px; line-height: 26px; color: #444; }

  .site-footer { position: absolute; left: 0; top: 569px; width: 1200px; height: 320px; color: var(--white); }
  .site-footer .brand { left: 142px; top: 48px; font-size: 24px; line-height: 30px; }
  .site-footer .brand-mark { width: 74px; height: 74px; }
  .social { position: absolute; left: 162px; top: 164px; display: flex; gap: 18px; }
  .social span { width: 34px; height: 34px; border: 1.5px solid var(--white); border-radius: 50%; }
  .foot-col { position: absolute; top: 50px; font-size: 15.5px; line-height: 29px; color: var(--white); }
  .foot-col h4 { font-family: "Montserrat", sans-serif; font-weight: 500; font-size: 16px; letter-spacing: 0.5px; margin-bottom: 12px; }
  .foot-col a { display: block; color: var(--white); text-decoration: none; }
  .contact-row { display: flex; gap: 18px; }
  .contact-row svg { flex: none; margin-top: 6px; }
  .copyright { position: absolute; left: 0; width: 1200px; top: 268px; text-align: center; font-size: 15.5px; color: var(--white); }
</style>
</head>
<body>

<header class="site-header">
  <div class="brand"><span class="brand-mark"></span><span>HARBOR<br>FIELD<br>STAFFING</span></div>
  <nav class="nav">
    <a class="active" href="#">HOME</a><a href="#">ABOUT US</a><a href="#">SERVICES</a><a href="#">BLOG</a><a href="#">CONTACT</a>
  </nav>
  <a class="btn header-cta" href="#">CONTACT US</a>
</header>

<section class="hero">
  <div class="hero-photo" role="img" aria-label="White semi-truck with grain trailer driving through a golden harvested wheat field at sunset"></div>
  <div class="hero-shade"></div>
  <p class="abs hero-kicker">WELCOME TO</p>
  <h1 class="abs heading hero-title">HARBOR FIELD<br>STAFFING</h1>
  <p class="abs hero-text">Lorem ipsum dolor sit amet, consecteturcng elitsedo eiusmod<br>tempor incididunt ut la aluis ipsum suspendisse ultrices</p>
  <a class="btn" href="#">CONTACT US</a>
</section>

<section class="about">
  <div class="abs about-photo" role="img" aria-label="Smiling truck driver with arms crossed standing in front of a truck and trailer"><div class="frame"></div></div>
  <h2 class="abs heading about-title">ABOUT US</h2>
  <p class="abs about-lead">Lorem ipsum dolor sit amet, consectetur adipiscing elit, sed do eius mod tempor incididunt ut labore et dolore magna</p>
  <div class="abs about-copy copy">
    <p>Lorem ipsum dolor sit amet, consectetur adipiscing elit, sed deius mod tempor incididunt ut labore et dolore magna aliqua. Utminim veniam, quis nostrud exercitation ullaco laboris nisi ut aliquip ex ea commodo consequat. Dure dolor in reprehenderit in voluptate.</p>
    <p>Sed deius mod tempor incididunt ut labore et dolore magna aliqua. Utminim veniam, quis nostrud exercitation ullaco laboris.</p>
  </div>
  <a class="btn about-btn" href="#">CONTACT US</a>
</section>

<section class="services">
  <h2 class="abs heading services-title">OUR SERVICES</h2>
  <svg class="arrow" style="left:37px" width="34" height="20" viewBox="0 0 34 20" aria-hidden="true"><path d="M33 10H2M10 2L2 10l8 8" fill="none" stroke="#000" stroke-width="1.8"/></svg>
  <article class="service" style="left:111px">
    <div class="service-photo" role="img" aria-label="Aerial view of a grain truck on a road between green crop fields" style="background:linear-gradient(180deg,#6f8a2e 0%,#b08a45 45%,#5d7a30 100%)"></div>
    <h3>LONG-TERM AND<br>CONTRACT STAFFING</h3>
    <p>Lorem ipsum dolor sit amet, consectetur adipiscing elit, seddoti eiusmod tempor incididut labore dolor magna aliqa.</p>
  </article>
  <article class="service" style="left:448px">
    <div class="service-photo" role="img" aria-label="Dump truck driving on a dusty gravel road under a sunset sky" style="background:linear-gradient(180deg,#5f6f80 0%,#c8a57a 45%,#a7a29a 100%)"></div>
    <h3>SAFETY TRAINING AND<br>CERTIFICATIONS</h3>
    <p>Lorem ipsum dolor sit amet, consectetur adipiscing elit, seddoti eiusmod tempor incididut labore dolor magna aliqa.</p>
  </article>
  <article class="service" style="left:784px">
    <div class="service-photo" role="img" aria-label="Open truck trailer loaded with fresh vegetables beside a farm field" style="background:linear-gradient(90deg,#9bb07a 0%,#4d6a32 40%,#5b5f58 60%,#b8402e 85%,#4f8a3a 100%)"></div>
    <h3>DRIVER PLACEMENT FOR<br>SEASONAL WORK</h3>
    <p>Lorem ipsum dolor sit amet, consectetur adipiscing elit, seddoti eiusmod tempor incididut labore dolor magna aliqa.</p>
  </article>
  <svg class="arrow" style="left:1119px" width="34" height="20" viewBox="0 0 34 20" aria-hidden="true"><path d="M1 10h31M24 2l8 8-8 8" fill="none" stroke="#000" stroke-width="1.8"/></svg>
</section>

<section class="why">
  <h2 class="abs heading why-title">WHY CHOOSE US</h2>
  <div class="abs why-copy copy">
    <p>Lorem ipsum dolor sit amet, consectetur adipiscing elit, sed deius mod tempor incididunt ut labore et dolore magna aliqua. Utminim veniam, quis nostrud exercitation ullaco laboris nisi ut aliquip ex ea commodo consequat. Dure dolor in reprehenderit in voluptate.</p>
    <p>Sed deius mod tempor incididunt ut labore et dolore magna aliqua. Utminim veniam, quis nostrud exercitation ullaco laboris.</p>
  </div>
  <a class="btn why-btn" href="#">CONTACT US</a>
  <div class="abs why-photo" role="img" aria-label="Happy truck driver in the cab giving a thumbs up"><div class="frame"></div></div>
</section>

<div class="lower">
  <section class="blog">
    <h2 class="abs heading blog-title">LATEST BLOG</h2>
    <article class="post" style="left:112px">
      <h3>Nemo enim ipsam voluptem quia volup aspernatur</h3>
      <time>05 Oct 2024</time>
      <p>Lorem ipsum dolor sit amet, consec tetur adipiscing elit, sed do eiusmod tempor incididunt ut laboreet dolore magna aliqua. Quis ipsu suspendisse ultavisus commodo viverra.</p>
    </article>
    <article class="post" style="left:447px">
      <h3>Nemo enim ipsam voluptem quia volup aspernatur</h3>
      <time>05 Oct 2024</time>
      <p>Lorem ipsum dolor sit amet, consec tetur adipiscing elit, sed do eiusmod tempor incididunt ut laboreet dolore magna aliqua. Quis ipsu suspendisse ultavisus commodo viverra.</p>
    </article>
    <article class="post" style="left:780px">
      <h3>Nemo enim ipsam voluptem quia volup aspernatur</h3>
      <time>05 Oct 2024</time>
      <p>Lorem ipsum dolor sit amet, consec tetur adipiscing elit, sed do eiusmod tempor incididunt ut laboreet dolore magna aliqua. Quis ipsu suspendisse ultavisus commodo viverra.</p>
    </article>
  </section>

  <footer class="site-footer">
    <div class="brand"><span class="brand-mark"></span><span>HARBOR<br>FIELD<br>STAFFING</span></div>
    <div class="social">
      <span aria-label="Social profile 1"></span><span aria-label="Social profile 2"></span><span aria-label="Social profile 3"></span><span aria-label="Social profile 4"></span>
    </div>
    <div class="foot-col" style="left:483px">
      <h4>CONTACT</h4>
      <div class="contact-row">
        <svg width="16" height="20" viewBox="0 0 16 20" aria-hidden="true"><path d="M8 0a8 8 0 0 0-8 8c0 6 8 12 8 12s8-6 8-12a8 8 0 0 0-8-8zm0 11a3 3 0 1 1 0-6 3 3 0 0 1 0 6z" fill="#fff"/></svg>
        <span>Harbor Field Staffing,<br>Address comes here</span>
      </div>
      <div class="contact-row" style="margin-top:8px">
        <svg width="16" height="16" viewBox="0 0 16 16" aria-hidden="true"><path d="M3.5 0.5l3 3-1.8 2.2a10 10 0 0 0 5.6 5.6l2.2-1.8 3 3-2 2.5C7 15 1 9 1 2.5z" fill="#fff"/></svg>
        <span>+1555-014-2270<br>info@harborfieldstaffing.com</span>
      </div>
    </div>
    <div class="foot-col" style="left:765px">
      <h4>QUICK LINKS</h4>
      <a href="#">Home</a><a href="#">About</a><a href="#">Services</a><a href="#">Blog</a>
    </div>
    <div class="foot-col" style="left:953px">
      <h4>OTHER LINKS</h4>
      <a href="#">Terms &amp; Conditions</a><a href="#">Privacy Policy</a><a href="#">Cookies</a><a href="#">Contact</a>
    </div>
    <p class="copyright">2024 Harbor Field Staffing. All Rights Reserved.</p>
  </footer>
</div>

</body>
</html>
```